Modify an already created sticker/decal

I have product “Model Names” but I need this modified to a more universal “Horizontal in Orientation” so that it fits nicely on the product itself when printed as a sticker/decal. There will be (3) models to start with Trail Mule LX, Trail Mule SR, Trail Mule QVN model names. The branding needs to follow-through on all decals/stickers.

```html
<!DOCTYPE html>
<html lang="en">
<head>
<meta charset="utf-8">
<title>Trail Mule Model Decals</title>
<link rel="stylesheet" href="https://fonts.googleapis.com/css2?family=Krona+One&display=swap">
<style>
  :root {
    --green: #80bd41;
    --white: #ffffff;
    --steel-dark: #767676;
    --steel-light: #c4c4c4;
    --model-grey: #8e8e8e;
  }
  * { margin: 0; padding: 0; box-sizing: border-box; }
  html, body {
    width: 1200px; height: 646px; overflow: hidden;
    background: var(--white);
  }
  .sheet { position: relative; width: 1200px; height: 646px; }
  .decal {
    position: absolute; left: 49px;
    width: 1110px; height: 185px;
    font-family: "Krona One", "Arial Black", sans-serif;
  }
  .decal--lx  { top: 40px; }
  .decal--sr  { top: 233px; }
  .decal--qvn { top: 426px; }
  .decal__art { position: absolute; inset: 0; }
  .brand-mark {
    position: absolute; left: 50px; top: 34px;
    width: 366px; height: 116px;
    display: flex; align-items: center; justify-content: center;
    color: var(--green);
    font-size: 29px; letter-spacing: 0.5px; white-space: nowrap;
  }
  .series-name {
    position: absolute; left: 525px; top: 44px;
    color: var(--white);
    font-size: 41px; line-height: 45px; letter-spacing: 1px;
  }
  .model-code {
    position: absolute; left: 828px; top: 46px;
    width: 262px; height: 91px;
    display: flex; align-items: center; justify-content: center;
    color: var(--model-grey);
    font-size: 72px; letter-spacing: -1px; white-space: nowrap;
  }
  .decal--qvn .model-code { font-size: 64px; }
</style>
</head>
<body>
<main class="sheet">

  <section class="decal decal--lx">
    <svg class="decal__art" width="1110" height="185" viewBox="0 0 1110 185" aria-hidden="true">
      <defs>
        <linearGradient id="steel-lx" x1="0" x2="1" y1="0" y2="0">
          <stop offset="0" stop-color="#767676"/>
          <stop offset="0.45" stop-color="#c4c4c4"/>
          <stop offset="1" stop-color="#767676"/>
        </linearGradient>
      </defs>
      <rect x="4.7" y="4.7" width="1100.6" height="175.6" fill="#fff" stroke="url(#steel-lx)" stroke-width="9.4"/>
      <polygon points="442,9.4 1100.6,9.4 1100.6,175.6 522,175.6" fill="#80bd41"/>
      <polygon points="779,46 1100.6,46 1100.6,137 823,137" fill="#fff"/>
    </svg>
    <div class="brand-mark">TRAIL MULE XR</div>
    <h2 class="series-name">TRAIL<br>MULE</h2>
    <div class="model-code">LX</div>
  </section>

  <section class="decal decal--sr">
    <svg class="decal__art" width="1110" height="185" viewBox="0 0 1110 185" aria-hidden="true">
      <defs>
        <linearGradient id="steel-sr" x1="0" x2="1" y1="0" y2="0">
          <stop offset="0" stop-color="#767676"/>
          <stop offset="0.45" stop-color="#c4c4c4"/>
          <stop offset="1" stop-color="#767676"/>
        </linearGradient>
      </defs>
      <rect x="4.7" y="4.7" width="1100.6" height="175.6" fill="#fff" stroke="url(#steel-sr)" stroke-width="9.4"/>
      <polygon points="442,9.4 1100.6,9.4 1100.6,175.6 522,175.6" fill="#80bd41"/>
      <polygon points="779,46 1100.6,46 1100.6,137 823,137" fill="#fff"/>
    </svg>
    <div class="brand-mark">TRAIL MULE XR</div>
    <h2 class="series-name">TRAIL<br>MULE</h2>
    <div class="model-code">SR</div>
  </section>

  <section class="decal decal--qvn">
    <svg class="decal__art" width="1110" height="185" viewBox="0 0 1110 185" aria-hidden="true">
      <defs>
        <linearGradient id="steel-qvn" x1="0" x2="1" y1="0" y2="0">
          <stop offset="0" stop-color="#767676"/>
          <stop offset="0.45" stop-color="#c4c4c4"/>
          <stop offset="1" stop-color="#767676"/>
        </linearGradient>
      </defs>
      <rect x="4.7" y="4.7" width="1100.6" height="175.6" fill="#fff" stroke="url(#steel-qvn)" stroke-width="9.4"/>
      <polygon points="442,9.4 1100.6,9.4 1100.6,175.6 522,175.6" fill="#80bd41"/>
      <polygon points="779,46 1100.6,46 1100.6,137 823,137" fill="#fff"/>
    </svg>
    <div class="brand-mark">TRAIL MULE XR</div>
    <h2 class="series-name">TRAIL<br>MULE</h2>
    <div class="model-code">QVN</div>
  </section>

</main>
</body>
</html>
```